Ashford Church of Grace (this will be used for new church sign) sign will be 4'x8' and would like also listed Sunday School 9:00am Worship Service 10:30am.

Logo Text

ASHFORD CHURCH OF GRACE

```html
<!DOCTYPE html>
<html lang="en">
<head>
<meta charset="utf-8">
<title>Ashford Church of Grace – Sign</title>
<link rel="stylesheet" href="https://fonts.googleapis.com/css2?family=Josefin+Sans:wght@300&family=Montserrat:wght@800&family=Poppins:wght@600&display=swap">
<style>
  :root {
    --crimson: #b91f43;
    --gold: #c7a72e;
    --paper: #ffffff;
    --mist: #e6e6e8;
  }
  * { margin: 0; padding: 0; box-sizing: border-box; }
  html, body { width: 720px; height: 1200px; overflow: hidden; background: var(--paper); }
  .sign {
    position: relative;
    width: 720px;
    height: 1200px;
    overflow: hidden;
    background:
      radial-gradient(ellipse at 25% 45%, var(--paper) 0%, rgba(255,255,255,0) 60%),
      linear-gradient(160deg, var(--paper) 0%, var(--mist) 35%, var(--paper) 55%, var(--mist) 100%);
    color: var(--crimson);
  }
  .brand {
    position: absolute;
    left: 36px;
    top: 122px;
    display: flex;
    align-items: center;
    gap: 22px;
  }
  .brand-dot {
    width: 90px;
    height: 90px;
    border-radius: 50%;
    background: var(--gold);
  }
  .brand-name {
    font-family: "Poppins", sans-serif;
    font-weight: 600;
    font-size: 33px;
    color: var(--crimson);
    white-space: nowrap;
  }
  .emblem-area {
    position: absolute;
    left: 430px;
    top: 221px;
    width: 290px;
    height: 470px;
    background: linear-gradient(150deg, var(--gold) 0%, #c46a3a 55%, var(--crimson) 100%);
    opacity: 0.85;
  }
  .headline {
    position: absolute;
    left: 16px;
    top: 622px;
    white-space: nowrap;
  }
  .headline-light {
    display: block;
    font-family: "Josefin Sans", sans-serif;
    font-weight: 300;
    font-size: 70px;
    line-height: 70px;
  }
  .headline-bold {
    display: block;
    margin-top: 6px;
    font-family: "Montserrat", sans-serif;
    font-weight: 800;
    font-size: 53px;
    line-height: 56px;
    letter-spacing: 0.5px;
  }
  .service {
    position: absolute;
    font-family: "Josefin Sans", sans-serif;
    font-weight: 300;
    font-size: 55px;
    line-height: 66px;
    color: var(--crimson);
    white-space: nowrap;
  }
  .service-sunday { left: 22px; top: 830px; }
  .service-worship { right: 32px; top: 952px; text-align: right; }
  .brackets { position: absolute; left: 0; top: 0; width: 720px; height: 1200px; pointer-events: none; }
  .brackets path { fill: none; stroke: var(--gold); stroke-width: 2; }
</style>
</head>
<body>
  <main class="sign">
    <header class="brand">
      <span class="brand-dot"></span>
      <span class="brand-name">Ashford Church of Grace</span>
    </header>

    <div class="emblem-area" role="img" aria-label="Large church emblem decoration in gold and crimson"></div>

    <h1 class="headline">
      <span class="headline-light">ASHFORD</span>
      <span class="headline-bold">CHURCH OF GRACE</span>
    </h1>

    <p class="service service-sunday">Sunday School<br>9:00am</p>
    <p class="service service-worship">Worship Service<br>10:30am</p>

    <svg class="brackets" viewBox="0 0 720 1200" aria-hidden="true">
      <path d="M406 862 H418 Q432 862 432 876 V922 Q432 936 418 936 H229"/>
      <path d="M313 983 H292 Q276 983 276 999 V1043 Q276 1059 292 1059 H457"/>
    </svg>
  </main>
</body>
</html>
```